Fenwell Building Partners Stationary Revamp

We need a full set of new stationary including business cards for our Public Sector Construction company based in the South East of England. We have a new logo (attached) that we want to launch and revamp all of our company literature. We are required to send a lot of correspondence to residents etc so a consistent theme is required across everything. Also attached is our existing templates.

Target Market(s)

We work for Council and government provided housing organisations and NOT private individuals. All of our clients represent government spent money, so we need to look professional and instantly recognisable brand.

Industry/Entity Type

Business

Colors

Designer to choose colors to be used in the design.

Requirements
Must have
• New fresh designs that utilise our new logo. And the letterhead needs to be able to be rolled out onto a word template so that all staff can type straight onto it rather than us having to have it printed first.
Nice to have
• I am looking forward to seeing your best efforts as designers.

```html
<!DOCTYPE html>
<html lang="en">
<head>
<meta charset="utf-8">
<title>Fenwell Building Partners – Stationery Set</title>
<link href="https://fonts.googleapis.com/css2?family=Roboto:wght@400;500;700&family=Open+Sans:wght@400&display=swap" rel="stylesheet">
<style>
:root{
  --backdrop:#868686;
  --paper:#f7f7f7;
  --paper-soft:#f1f1f1;
  --ink:#231a17;
  --text:#555555;
  --muted:#777777;
  --gold:#d4a80f;
  --gold-light:#efc52a;
  --white:#ffffff;
}
*{margin:0;padding:0;box-sizing:border-box}
html,body{width:1200px;height:641px;overflow:hidden;background:var(--backdrop)}
.canvas{position:relative;width:1200px;height:641px;overflow:hidden;background:var(--backdrop);font-family:"Roboto",sans-serif;color:var(--text)}

.brand{display:flex;align-items:center;gap:6px;font-family:"Roboto",sans-serif;font-weight:700;color:var(--ink);line-height:1.05}
.brand__dot{flex:none;border-radius:50%;background:var(--gold)}

/* Letterhead */
.letterhead{position:absolute;left:227px;top:28px;width:417px;height:586px;background:var(--paper);overflow:hidden}
.letterhead .brand{position:absolute;left:25px;top:46px;font-size:12px;width:110px}
.letterhead .brand__dot{width:12px;height:12px}
.directors{position:absolute;right:122px;top:30px;text-align:right;font-size:6.4px;line-height:8.3px;color:var(--muted)}
.head-divider{position:absolute;left:304px;top:31px;width:1px;height:70px;background:#bbb}
.head-contact{position:absolute;left:313px;top:30px;font-size:6.4px;line-height:8.3px;color:var(--muted)}
.contact-line{display:flex;align-items:center;gap:4px}
.icon{flex:none;width:6px;height:6px;fill:var(--gold)}
.salutation{position:absolute;left:25px;top:148px;font-family:"Open Sans",sans-serif;font-size:12px;color:#555}
.letter-body{position:absolute;left:25px;top:182px;width:372px;font-family:"Open Sans",sans-serif;font-size:6.85px;line-height:10.7px;color:#555}
.letter-body p{margin-bottom:10.5px}
.signoff{position:absolute;left:25px;top:406px;font-family:"Open Sans",sans-serif;font-size:6.85px;color:#555}
.signature{position:absolute;left:24px;top:420px;width:58px;height:18px;background:linear-gradient(90deg,#e6e6e6,#d8d8d8);border-radius:3px}
.accreditations{position:absolute;left:26px;top:500px;display:flex;align-items:center;gap:5px}
.badge{background:#e2e2e2;border:1px solid #b8b8b8}
.badge--cert{width:56px;height:29px}
.badge--round{width:22px;height:22px;border-radius:50%;margin-left:18px}
.badge--small{width:16px;height:22px;margin-left:20px}
.badge--wide{width:38px;height:20px}
.badge--flat{width:46px;height:18px}
.footer-swoosh{position:absolute;left:0;bottom:0;width:417px;height:55px}

/* Business card */
.card{position:absolute;left:38px;top:324px;width:165px;height:290px;border-radius:10px;background:var(--paper-soft);overflow:hidden}
.card__shape{position:absolute;left:0;top:0;width:165px;height:290px}
.card .brand{position:absolute;left:52px;top:54px;font-size:10px;width:100px}
.card .brand__dot{width:10px;height:10px}
.card__person{position:absolute;left:12px;top:174px;color:var(--white)}
.card__name{font-size:9.6px;font-weight:700;color:var(--gold-light);line-height:11px}
.card__role{font-size:7.6px;font-weight:500;line-height:10px;margin-bottom:4px}
.card__address{font-size:7px;line-height:9px;color:#eee}
.card__contact{margin-top:6px;font-size:7px;line-height:9px;color:#eee}

/* Envelopes */
.envelope{position:absolute;left:668px;width:466px;background:var(--paper)}
.envelope--back{top:176px;height:212px}
.envelope--front{top:400px;height:214px;overflow:hidden}
.flap{position:absolute;left:0;top:0;width:466px;height:79px}
.flap-content{position:absolute;left:0;top:22px;width:466px;display:flex;flex-direction:column;align-items:center;gap:6px;color:var(--white)}
.flap-content .brand{color:var(--white);font-size:9px}
.flap-content .brand__dot{width:8px;height:8px}
.flap-url{font-size:6.4px;font-weight:500;letter-spacing:.3px}
.envelope--front .brand{position:absolute;left:22px;top:40px;font-size:10px;width:100px}
.envelope--front .brand__dot{width:10px;height:10px}
.return-address{position:absolute;left:22px;top:92px;font-size:6.8px;line-height:8.6px;color:var(--muted)}
.envelope--front .footer-swoosh{width:466px;height:48px}
</style>
</head>
<body>
<div class="canvas">

  <article class="card">
    <svg class="card__shape" viewBox="0 0 165 290" preserveAspectRatio="none" aria-hidden="true">
      <path d="M0 68 C40 140 100 185 165 188 L165 290 L0 290 Z" fill="var(--gold)"/>
      <path d="M0 74 C40 146 100 190 165 193 L165 290 L0 290 Z" fill="var(--ink)"/>
    </svg>
    <div class="brand"><span class="brand__dot"></span>Fenwell Building Partners</div>
    <div class="card__person">
      <div class="card__name">R J HALE MIOD</div>
      <div class="card__role">MANAGING DIRECTOR</div>
      <div class="card__address">Marlow House<br>12 Larkfield Road<br>Ashford, Kent, TN23 4QP<br>Reg No: 09182736</div>
      <div class="card__contact">
        <div class="contact-line"><svg class="icon" viewBox="0 0 10 10"><path d="M2 0h2l1 3-1.5 1a6 6 0 0 0 2.5 2.5L7 5l3 1v2c0 1-1 2-2 2A8 8 0 0 1 0 2c0-1 1-2 2-2z"/></svg>020 7946 0321</div>
        <div class="contact-line"><svg class="icon" viewBox="0 0 10 10"><rect x="2" y="0" width="6" height="3"/><rect x="0" y="4" width="10" height="5" rx="1"/></svg>020 7946 0322</div>
        <div class="contact-line"><svg class="icon" viewBox="0 0 10 10"><path d="M0 2h10v6H0z M0 2l5 3 5-3" /></svg>info@fenwellbp.co.uk</div>
        <div class="contact-line"><svg class="icon" viewBox="0 0 10 10"><circle cx="5" cy="5" r="5"/></svg>www.fenwellbp.co.uk</div>
      </div>
    </div>
  </article>

  <article class="letterhead">
    <div class="brand"><span class="brand__dot"></span>Fenwell Building Partners</div>
    <div class="directors">
      R J Hale MIOD<br>Managing Director<br>M T Carver BSc<br>Directors<br>D K Ashby<br>L Pryce CMIOSH<br>Group Companies<br>Fenwell Interiors Ltd<br>Fenwell Green Services Ltd
    </div>
    <div class="head-divider"></div>
    <div class="head-contact">
      Marlow House<br>12 Larkfield Road<br>Ashford, Kent, TN23 4QP<br>Reg No: 09182736
      <div class="contact-line"><svg class="icon" viewBox="0 0 10 10"><path d="M2 0h2l1 3-1.5 1a6 6 0 0 0 2.5 2.5L7 5l3 1v2c0 1-1 2-2 2A8 8 0 0 1 0 2c0-1 1-2 2-2z"/></svg>020 7946 0321</div>
      <div class="contact-line"><svg class="icon" viewBox="0 0 10 10"><rect x="2" y="0" width="6" height="3"/><rect x="0" y="4" width="10" height="5" rx="1"/></svg>020 7946 0322</div>
      <div class="contact-line"><svg class="icon" viewBox="0 0 10 10"><path d="M0 2h10v6H0z"/></svg>info@fenwellbp.co.uk</div>
      <div class="contact-line"><svg class="icon" viewBox="0 0 10 10"><circle cx="5" cy="5" r="5"/></svg>www.fenwellbp.co.uk</div>
    </div>

    <p class="salutation">Dear Mr. Bennett,</p>
    <div class="letter-body">
      <p>Lorem ipsum dolor sit amet, consectetur adipiscing elit. Donec orci purus, luctus vitae dignissim eu, iaculis sed purus. Vivamus faucibus, ipsum nec aliquet viverra, leo mauris condimentum ligula, sit amet sagittis enim ligula quis arcu. Nam egestas tortor id nisi porttitor mattis. In tortor ante, ultricies in suscipit a, tempus non massa. Vivamus et auctor mi. Fusce vel massa nulla. Phasellus nec eros mauris, et scelerisque orci.</p>
      <p>Donec malesuada orci vitae nulla accumsan porta a id massa. Quisque accumsan iaculis magna sit amet fringilla. Maecenas consequat, magna eget tincidunt semper, odio nibh rutrum mi, id feugiat ante nisi eu risus. Vestibulum nunc orci, rhoncus a placerat in, ultricies in mi. Cras mattis varius eros, vel fringilla nisi suscipit eget. Quisque scelerisque sagittis nulla at porttitor.</p>
      <p>Sed id augue vitae urna euismod commodo aliquet a quam. Pellentesque arcu velit, cursus et malesuada ut, consequat et diam. Nullam erat sem, rhoncus id ullamcorper vitae, rhoncus et arcu. In ultricies ultricies nulla, ut rutrum nisi iaculis at. Donec eu magna a metus ornare faucibus. Fusce aliquet faucibus ultricies. Morbi semper, est id tincidunt gravida, sem arcu adipiscing lacus, ac bibendum nulla leo eu purus. Quisque nec diam sed risus consectetur a ccumsan quis quis nibh. Vestibulum id purus lorem.</p>
      <p>It is a long established fact that a reader will be distracted by the readable content of a page when looking at its layout. The point of using Lorem Ipsum is that it has a more-or-less normal distribution of letters, as opposed to using 'Content here, content here', making it look like readable English. Many desktop publishing packages</p>
    </div>
    <p class="signoff">Sincerely,</p>
    <div class="signature" role="img" aria-label="Handwritten signature of the managing director"></div>

    <div class="accreditations">
      <div class="badge badge--cert"></div>
      <div class="badge badge--cert"></div>
      <div class="badge badge--cert"></div>
      <div class="badge badge--round"></div>
      <div class="badge badge--small"></div>
      <div class="badge badge--wide"></div>
      <div class="badge badge--flat"></div>
    </div>

    <svg class="footer-swoosh" viewBox="0 0 417 55" preserveAspectRatio="none" aria-hidden="true">
      <path d="M0 38 C150 40 320 30 417 0 L417 55 L0 55 Z" fill="var(--gold)"/>
      <path d="M0 42 C150 44 320 34 417 5 L417 55 L0 55 Z" fill="var(--ink)"/>
    </svg>
  </article>

  <article class="envelope envelope--back">
    <svg class="flap" viewBox="0 0 466 79" preserveAspectRatio="none" aria-hidden="true">
      <path d="M0 0 H466 L450 50 Q442 79 410 79 H56 Q24 79 16 50 Z" fill="var(--ink)"/>
    </svg>
    <div class="flap-content">
      <div class="brand"><span class="brand__dot"></span>Fenwell Building Partners</div>
      <div class="flap-url">WWW.FENWELLBP.CO.UK</div>
    </div>
  </article>

  <article class="envelope envelope--front">
    <div class="brand"><span class="brand__dot"></span>Fenwell Building Partners</div>
    <div class="return-address">Marlow House<br>12 Larkfield Road<br>Ashford, Kent, TN23 4QP<br>Reg No: 09182736</div>
    <svg class="footer-swoosh" viewBox="0 0 466 48" preserveAspectRatio="none" aria-hidden="true">
      <path d="M0 26 C170 28 360 20 466 0 L466 48 L0 48 Z" fill="var(--gold)"/>
      <path d="M0 30 C170 32 360 24 466 5 L466 48 L0 48 Z" fill="var(--ink)"/>
    </svg>
  </article>

</div>
</body>
</html>
```